Design a Website Mockup for Car Rental "MOBILE ONLY"

Hi,

I want to design a mobile version for the attached images.
Please use the same information and same colors.

Good luck!
TERIK

```html
<!DOCTYPE html>
<html lang="en">
<head>
<meta charset="utf-8">
<title>Car Rental Mobile Booking</title>
<link href="https://fonts.googleapis.com/css2?family=Open+Sans:wght@400;600;700&display=swap" rel="stylesheet">
<style>
:root{
  --bg:#0d3c73;
  --screen:#ffffff;
  --blue:#1f72c4;
  --blue-dark:#155a9f;
  --blue-light:#3d94e0;
  --text:#333333;
  --muted:#8a8a8a;
  --field:#f1f1f1;
  --field-border:#c9c9c9;
  --grey-band:#e6e6e6;
  --red:#d0021b;
}
*{box-sizing:border-box;margin:0;padding:0}
html,body{width:1200px;height:800px;overflow:hidden}
body{background:var(--bg);font-family:"Open Sans",Arial,sans-serif;color:var(--text);position:relative}
.screen{position:absolute;top:141px;width:296px;height:517px;background:var(--screen);overflow:hidden;border:1px solid #9aa7b5}
.screen--form{left:276px}
.screen--rate{left:629px}
.steps{display:block;width:296px;height:45px}
.steps text{font-family:"Open Sans",Arial,sans-serif;font-weight:700;font-size:15px}
.form{padding:6px 12px 0}
.label{font-size:8.5px;color:#555;margin-top:4px}
.label b{font-weight:700;color:#222}
.select{position:relative;height:25px;border:1px solid var(--field-border);background:var(--field);font-size:11px;color:#9a9a9a;line-height:23px;padding-left:8px;margin-top:2px}
.select::after{content:"";position:absolute;right:0;top:0;width:20px;height:23px;border-left:1px solid var(--field-border);background:#e3e3e3}
.select .caret{position:absolute;right:6px;top:9px;width:0;height:0;border-left:4px solid transparent;border-right:4px solid transparent;border-top:5px solid #666;z-index:1}
.row{display:flex;gap:8px}
.col{flex:1}
.date{display:flex;align-items:center;gap:4px;margin-top:2px}
.date .select{flex:1;margin-top:0}
.date .select::after,.date .select .caret{display:none}
.specs{display:flex;align-items:center;margin-top:10px;height:62px}
.spec-grid{display:grid;grid-template-columns:repeat(2,60px);row-gap:4px;font-size:8px}
.spec{display:flex;align-items:center;gap:6px}
.car{margin-left:auto;width:120px;height:46px;border-radius:22px 30px 10px 10px;background:linear-gradient(180deg,#4aa0c8,#1c5f86)}
.car-wrap{margin-left:auto;text-align:center;font-size:8px;color:var(--blue)}
.note{font-size:8px;color:var(--red);margin-top:3px}
.vip{margin-top:10px;height:24px;background:linear-gradient(180deg,var(--blue-light),var(--blue-dark));color:#fff;font-size:8.5px;font-weight:700;display:flex;align-items:center;padding:0 12px;gap:8px}
.vip .more{margin-left:auto}
.options{display:flex;padding:12px 12px 0;font-size:8.5px}
.options .col{display:flex;flex-direction:column;gap:8px}
.opt{display:flex;align-items:center;gap:8px}
.radio{width:9px;height:9px;border:1px solid #888;border-radius:50%;background:#fff;position:relative;flex:none}
.radio.on::after{content:"";position:absolute;left:2px;top:2px;width:3px;height:3px;border-radius:50%;background:#333}
.check{width:9px;height:9px;border:1px solid #888;background:#fff;flex:none;position:relative}
.check svg{position:absolute;left:-1px;top:-3px}
.btn{display:inline-block;background:linear-gradient(180deg,#5aa8ec,var(--blue-dark));color:#fff;font-weight:700;border-radius:4px;text-align:center}
.btn--rate{width:138px;height:38px;line-height:38px;font-size:13px;margin-top:6px}
.class-title{font-size:12px;font-weight:700;padding:6px 12px 0;color:#222}
.class-title span{font-weight:400;color:var(--blue)}
.rate-specs{padding:0 12px}
.rates{margin-top:10px;font-size:7.5px}
.rates .r{display:flex;justify-content:space-between;padding:0 12px;height:18px;line-height:18px;background:var(--grey-band);border-bottom:1px solid #fff}
.total{display:flex;height:22px;line-height:22px;background:linear-gradient(180deg,var(--blue-light),var(--blue-dark));color:#fff;font-size:7.5px}
.total .details{width:86px;text-align:center;background:rgba(0,0,0,.15)}
.total .sum{flex:1;display:flex;justify-content:space-between;padding:0 12px 0 14px;font-weight:700}
.extra{display:flex;background:#f4f4f4;height:62px;border-bottom:1px solid #ddd}
.extra .col{padding:6px 8px}
.extra .col+.col{border-left:1px solid #ddd;text-align:center}
.extra h3{font-size:10px;font-weight:400;color:var(--blue);margin-bottom:8px}
.extra .opt{font-size:7px;gap:5px;margin-bottom:6px}
.btn--learn{width:80px;height:18px;line-height:18px;font-size:7.5px;margin-top:6px}
</style>
</head>
<body>

<section class="screen screen--form">
  <svg class="steps" viewBox="0 0 296 45" aria-label="Booking steps, step 1 active">
    <defs>
      <linearGradient id="stepGrey" x1="0" y1="0" x2="0" y2="1"><stop offset="0" stop-color="#fafafa"/><stop offset="1" stop-color="#dcdcdc"/></linearGradient>
      <linearGradient id="stepBlue" x1="0" y1="0" x2="0" y2="1"><stop offset="0" stop-color="#3d94e0"/><stop offset="1" stop-color="#155a9f"/></linearGradient>
    </defs>
    <rect width="296" height="45" fill="url(#stepGrey)"/>
    <polyline points="196,0 210,22.5 196,45" fill="none" stroke="#b5b5b5"/>
    <polygon points="0,0 94,0 108,22.5 94,45 0,45" fill="url(#stepBlue)"/>
    <text x="26" y="28" fill="#fff">STEP 1</text>
    <text x="124" y="28" fill="#1f5f9f">STEP 2</text>
    <text x="222" y="28" fill="#1f5f9f">STEP 3</text>
  </svg>

  <div class="form">
    <div class="label"><b>Pickup</b> location</div>
    <div class="select">Tap here to choose<i class="caret"></i></div>

    <div class="row">
      <div class="col">
        <div class="label"><b>Pickup</b> date</div>
        <div class="date">
          <svg width="18" height="18" viewBox="0 0 18 18"><rect x="1" y="3" width="16" height="14" rx="2" fill="#e9e9e9" stroke="#999"/><rect x="1" y="3" width="16" height="5" fill="#c0392b"/><path d="M4 11h2M8 11h2M12 11h2M4 14h2M8 14h2" stroke="#777"/></svg>
          <div class="select">10 Dec 2013</div>
        </div>
      </div>
      <div class="col">
        <div class="label"><b>Pickup</b> time</div>
        <div class="select">10:22<i class="caret"></i></div>
      </div>
    </div>

    <div class="label"><b>Return</b> location</div>
    <div class="select">Tap here to choose<i class="caret"></i></div>

    <div class="row">
      <div class="col">
        <div class="label"><b>Return</b> date</div>
        <div class="date">
          <svg width="18" height="18" viewBox="0 0 18 18"><rect x="1" y="3" width="16" height="14" rx="2" fill="#e9e9e9" stroke="#999"/><rect x="1" y="3" width="16" height="5" fill="#c0392b"/><path d="M4 11h2M8 11h2M12 11h2M4 14h2M8 14h2" stroke="#777"/></svg>
          <div class="select">15 Dec 2013</div>
        </div>
      </div>
      <div class="col">
        <div class="label"><b>Return</b> time</div>
        <div class="select">10:22<i class="caret"></i></div>
      </div>
    </div>

    <div class="specs">
      <div class="spec-grid">
        <div class="spec"><svg width="14" height="14" viewBox="0 0 14 14"><rect x="1" y="3" width="12" height="10" rx="1" fill="#ccc" stroke="#888"/><rect x="5" y="1" width="4" height="2" fill="none" stroke="#888"/></svg>1</div>
        <div class="spec"><svg width="14" height="14" viewBox="0 0 14 14"><circle cx="7" cy="4" r="3" fill="#b08a5a"/><rect x="2" y="8" width="10" height="6" rx="3" fill="#7a8a99"/></svg>2</div>
        <div class="spec"><svg width="14" height="14" viewBox="0 0 14 14"><rect x="2" y="4" width="10" height="8" rx="1" fill="#a0522d"/><rect x="5" y="2" width="4" height="2" fill="none" stroke="#a0522d"/></svg>2</div>
        <div class="spec"><svg width="14" height="14" viewBox="0 0 14 14"><circle cx="7" cy="4" r="3" fill="#b08a5a"/><rect x="2" y="8" width="10" height="6" rx="3" fill="#555"/></svg>3</div>
        <div class="spec"><svg width="14" height="14" viewBox="0 0 14 14" stroke="#1f72c4" stroke-width="1.6"><path d="M7 1v12M1.8 4l10.4 6M1.8 10l10.4-6"/></svg>AC</div>
        <div class="spec"><svg width="14" height="14" viewBox="0 0 14 14" fill="none" stroke="#333"><circle cx="7" cy="7" r="6"/><path d="M5 4v6M9 4v6M5 7h4"/></svg>Auto</div>
      </div>
      <div class="car-wrap">
        <div class="car" role="img" aria-label="Photo of a blue compact hatchback"></div>
        <div>Veloce 2 or similar</div>
      </div>
    </div>

    <div class="label"><b>Select</b> car type</div>
    <div class="select">E - Veloce 2 (or similar)<i class="caret"></i></div>
    <div class="note">Please select <b>pickup</b> and <b>return</b> location</div>
  </div>

  <div class="vip"><svg width="9" height="9" viewBox="0 0 9 9"><circle cx="4.5" cy="4.5" r="4" fill="#fff"/></svg>VIP GOLD Club<span class="more">Learn More ›</span></div>

  <div class="options">
    <div class="col">
      <div class="opt"><span class="radio on"></span>Comprehensive</div>
      <div class="opt"><span class="radio"></span>Mandatory 3<sup>rd</sup> party liability</div>
      <span class="btn btn--rate">GET RATE</span>
    </div>
    <div class="col" style="flex:0 0 90px">
      <div class="opt"><span class="check"><svg width="11" height="11" viewBox="0 0 11 11"><path d="M2 6l3 3 5-8" fill="none" stroke="#1f72c4" stroke-width="2"/></svg></span>Additional Driver</div>
      <div class="opt"><span class="check"></span>Baby Seat</div>
      <div class="opt"><span class="check"></span>Booster</div>
      <div class="opt"><span class="check"><svg width="11" height="11" viewBox="0 0 11 11"><path d="M2 6l3 3 5-8" fill="none" stroke="#1f72c4" stroke-width="2"/></svg></span>Tablet</div>
    </div>
  </div>
</section>

<section class="screen screen--rate">
  <svg class="steps" viewBox="0 0 296 45" aria-label="Booking steps, step 2 active">
    <rect width="296" height="45" fill="url(#stepGrey)"/>
    <polyline points="90,0 104,22.5 90,45" fill="none" stroke="#b5b5b5"/>
    <polygon points="96,0 192,0 206,22.5 192,45 96,45 110,22.5" fill="url(#stepBlue)"/>
    <text x="22" y="28" fill="#1f5f9f">STEP 1</text>
    <text x="124" y="28" fill="#fff">STEP 2</text>
    <text x="222" y="28" fill="#1f5f9f">STEP 3</text>
  </svg>

  <div class="class-title">CLASS E: <span>Veloce 2 or similar</span></div>
  <div class="rate-specs">
    <div class="specs" style="margin-top:4px">
      <div class="spec-grid">
        <div class="spec"><svg width="14" height="14" viewBox="0 0 14 14"><rect x="1" y="3" width="12" height="10" rx="1" fill="#ccc" stroke="#888"/><rect x="5" y="1" width="4" height="2" fill="none" stroke="#888"/></svg>1</div>
        <div class="spec"><svg width="14" height="14" viewBox="0 0 14 14"><circle cx="7" cy="4" r="3" fill="#b08a5a"/><rect x="2" y="8" width="10" height="6" rx="3" fill="#7a8a99"/></svg>2</div>
        <div class="spec"><svg width="14" height="14" viewBox="0 0 14 14"><rect x="2" y="4" width="10" height="8" rx="1" fill="#a0522d"/><rect x="5" y="2" width="4" height="2" fill="none" stroke="#a0522d"/></svg>2</div>
        <div class="spec"><svg width="14" height="14" viewBox="0 0 14 14"><circle cx="7" cy="4" r="3" fill="#b08a5a"/><rect x="2" y="8" width="10" height="6" rx="3" fill="#555"/></svg>3</div>
        <div class="spec"><svg width="14" height="14" viewBox="0 0 14 14" stroke="#1f72c4" stroke-width="1.6"><path d="M7 1v12M1.8 4l10.4 6M1.8 10l10.4-6"/></svg>AC</div>
        <div class="spec"><svg width="14" height="14" viewBox="0 0 14 14" fill="none" stroke="#333"><circle cx="7" cy="7" r="6"/><path d="M5 4v6M9 4v6M5 7h4"/></svg>Auto</div>
      </div>
      <div class="car" role="img" aria-label="Photo of a blue compact hatchback"></div>
    </div>
  </div>

  <div class="rates">
    <div class="r"><span>Rate before discount</span><span>$ 228.62</span></div>
    <div class="r"><span>Internet discount</span><span>$ 27.52</span></div>
    <div class="r"><span>Airport fee</span><span>$ 28.00</span></div>
  </div>
  <div class="total"><span class="details">View Rate Details</span><span class="sum"><span>Total after discount</span><span>$ 229.10</span></span></div>

  <div class="extra">
    <div class="col">
      <h3>Complete your reservation</h3>
      <div class="opt"><span class="radio on"></span>F for only $ 6.55 a day</div>
      <div class="opt"><span class="radio"></span>I for only $ 0.50 a day</div>
    </div>
    <div class="col">
      <h3 style="display:flex;gap:6px;justify-content:center;align-items:center"><span class="check"><svg width="11" height="11" viewBox="0 0 11 11"><path d="M2 6l3 3 5-8" fill="none" stroke="#1f72c4" stroke-width="2"/></svg></span>Harlan's Expressway</h3>
      <span class="btn btn--learn">Learn More</span>
    </div>
  </div>
</section>

</body>
</html>
```